Luxury WordPress Website for CORALBASINS

I need a professional WordPress website for Coral Basins. The site should be modern, visually appealing, and user-friendly, reflecting the brand’s luxury and premium identity. It must include a homepage, product/service pages, contact form, and be responsive on both desktop and mobile devices. The design should allow for easy updates and integration of future content, while maintaining a polished and professional look.

Target Market(s)

swimmingpool & spa

Industry/Entity Type

Swimmingpool

Coding

Coded - Design and coding required

Font styles to use
Other font styles liked:
• HaboroSoft

Requirements
Must have
• Exclusive appearance
Nice to have
• • A logo that subtly incorporates water or pool elements. • A color palette that reflects luxury, elegance, and relaxation. • Clean and modern typography that is easy to read across all media. • Iconography or design elements that convey premium quality. • A versatile design that can be adapted for social media, merchandise, and promotional materials. • Optional: A tagline that emphasizes luxury and high-end pool experiences.

```html
<!DOCTYPE html>
<html lang="en">
<head>
<meta charset="utf-8">
<title>Coral Basins — Crafting Timeless Luxury Pools</title>
<link href="https://fonts.googleapis.com/css2?family=Nunito+Sans:wght@400;600;700&family=Source+Sans+3:wght@400;600&family=Oswald:wght@500;600;700&family=Montserrat:wght@400;500;600&display=swap" rel="stylesheet">
<style>
:root{
  --blue:#0a5cff;
  --navy:#1557b6;
  --ink:#1f1f1f;
  --muted:#555;
  --line:#e4e4e4;
  --white:#fff;
  --star:#f3a316;
  --footer-bar:#1557b6;
}
*{margin:0;padding:0;box-sizing:border-box}
html,body{width:1200px;height:5240px;overflow:hidden}
body{position:relative;background:var(--white);font-family:"Source Sans 3",sans-serif;color:var(--ink)}
.abs{position:absolute}
.btn{position:absolute;display:flex;align-items:center;justify-content:center;background:var(--blue);color:var(--white);font-family:"Oswald",sans-serif;font-weight:600;font-size:16px;box-shadow:0 4px 10px rgba(10,92,255,.35)}
.btn-outline{position:absolute;display:flex;align-items:center;justify-content:center;border:2px solid #c4cfe0;border-radius:8px;color:var(--navy);font-family:"Oswald",sans-serif;font-weight:600;font-size:13px}

/* hero */
.hero{left:0;top:0;width:1200px;height:733px;background:linear-gradient(180deg,#8fa7a6 0%,#b6c6c0 35%,#3f9ac0 60%,#6f7980 100%)}
.hero::after{content:"";position:absolute;inset:0;background:rgba(20,40,50,.25)}
.brand{left:92px;top:52px;display:flex;align-items:center;gap:10px;z-index:2;font-family:"Nunito Sans",sans-serif;font-weight:600;font-size:16px;color:var(--white);letter-spacing:1px}
.brand .dot{width:22px;height:22px;border-radius:50%;background:rgba(255,255,255,.85)}
.nav{top:62px;z-index:2;color:var(--white);font-family:"Montserrat",sans-serif;font-weight:500;font-size:15px}
.hero-title{left:0;width:1200px;top:320px;text-align:center;z-index:2;color:var(--white);font-family:"Nunito Sans",sans-serif;font-weight:400;font-size:49px}
.hero-sub{left:0;width:1200px;top:414px;text-align:center;z-index:2;color:var(--white);font-size:22px;line-height:31px}

.section-title{left:0;width:1200px;text-align:center;font-family:"Nunito Sans",sans-serif;font-weight:400;font-size:28px;color:var(--ink)}
.section-sub{left:0;width:1200px;text-align:center;font-size:22px;line-height:31px;color:var(--muted)}

.photo{position:absolute}
.about-text{left:667px;top:1088px;width:480px;font-size:22px;line-height:31.5px;color:var(--muted)}

.service-card{position:absolute;top:1696px;height:474px;color:var(--white)}
.service-card h3{position:absolute;left:28px;font-family:"Nunito Sans",sans-serif;font-weight:600;font-size:25px;line-height:31px}
.service-card p{position:absolute;left:28px;right:28px;font-size:12px;line-height:17px}

.style-title{position:absolute;top:2896px;width:340px;text-align:center;font-family:"Oswald",sans-serif;font-weight:600;font-size:20px;color:var(--navy)}
.style-desc{position:absolute;top:2944px;width:340px;text-align:center;font-family:"Montserrat",sans-serif;font-weight:500;font-size:13px;line-height:21px;color:var(--navy)}

.review{position:absolute;top:3291px;width:455px;height:323px;border:1px solid var(--line);background:var(--white);box-shadow:0 2px 6px rgba(0,0,0,.05)}
.review .avatar{position:absolute;left:26px;top:26px;width:65px;height:65px}
.review .stars{position:absolute;right:22px;top:30px;display:flex;gap:6px}
.review h4{position:absolute;left:26px;top:110px;font-family:"Montserrat",sans-serif;font-weight:500;font-size:26px}
.review p{position:absolute;left:26px;top:152px;width:410px;font-family:"Montserrat",sans-serif;font-size:18px;line-height:24.5px;color:#444}

/* contact */
.contact{left:0;top:3872px;width:1200px;height:928px;background:var(--navy);color:var(--white)}
.contact h2{position:absolute;left:118px;top:110px;font-family:"Oswald",sans-serif;font-weight:700;font-size:52px}
.contact .lead{position:absolute;left:118px;top:220px;font-family:"Oswald",sans-serif;font-weight:400;font-size:17px;line-height:27px;opacity:.9}
.contact .ico{position:absolute;left:122px;width:70px;height:70px;border-radius:50%;border:2px solid var(--white);background:rgba(255,255,255,.05);display:flex;align-items:center;justify-content:center}
.contact .ico.solid{background:var(--white)}
.contact .info{position:absolute;left:218px;font-family:"Montserrat",sans-serif;font-size:15px;line-height:20px}
.contact .info b{font-weight:600;display:block}
.field-label{position:absolute;left:606px;font-family:"Montserrat",sans-serif;font-weight:600;font-size:15px;letter-spacing:.5px}
.field{position:absolute;left:606px;width:507px;border:1.5px solid rgba(255,255,255,.75)}
.submit{position:absolute;left:606px;top:737px;width:163px;height:39px;background:var(--white);color:var(--navy);display:flex;align-items:center;justify-content:center;font-family:"Oswald",sans-serif;font-weight:600;font-size:13px}

/* footer */
.footer{font-family:"Montserrat",sans-serif}
.foot-head{position:absolute;top:4908px;font-weight:600;font-size:14px;color:var(--navy);letter-spacing:.3px}
.foot-head::after{content:"";display:block;width:50px;height:2px;background:var(--navy);margin-top:6px}
.foot-link{position:absolute;font-size:14px;color:var(--navy);line-height:19px}
.copy{left:0;top:5191px;width:1200px;height:49px;background:var(--footer-bar);color:var(--white);display:flex;align-items:center;justify-content:center;font-family:"Montserrat",sans-serif;font-weight:500;font-size:14px}
</style>
</head>
<body>

<!-- HERO -->
<div class="abs hero" role="img" aria-label="Resort poolside terrace with parasol and loungers beside a blue pool, palm trees behind"></div>
<div class="abs brand"><span class="dot"></span>CORAL BASINS</div>
<div class="abs nav" style="left:380px">HOME</div>
<div class="abs nav" style="left:480px">ABOUT US</div>
<div class="abs nav" style="left:618px">SERVICE</div>
<div class="abs nav" style="left:734px">TESTIMONY</div>
<div class="btn" style="left:976px;top:53px;width:173px;height:39px;z-index:2;box-shadow:none">Contact Us</div>
<h1 class="abs hero-title">Crafting Timeless Luxury Pools</h1>
<p class="abs hero-sub">Experience the perfect harmony of design, durability, and sophistication<br>where every pool is a statement of elegance.</p>
<div class="btn" style="left:513px;top:529px;width:170px;height:41px;z-index:2;font-size:15px">Request a Consultation</div>

<!-- ABOUT -->
<h2 class="abs section-title" style="top:804px">Redefining Luxury Pool Living</h2>
<p class="abs section-sub" style="top:868px">Where craftsmanship meets elegance &nbsp;creating pools that inspire<br>relaxation, beauty, and timeless sophistication.</p>
<div class="photo" style="left:61px;top:1009px;width:566px;height:376px;background:linear-gradient(180deg,#e8e8e6 0%,#cfcac3 55%,#5fb8c8 85%,#3aa3b5 100%)" role="img" aria-label="Guests relaxing on white cabana daybeds beside a pool"></div>
<h2 class="abs" style="left:667px;top:1008px;font-family:'Nunito Sans',sans-serif;font-weight:400;font-size:28px">Coral Basins</h2>
<div class="abs" style="left:667px;top:1056px;width:116px;height:5px;background:var(--blue)"></div>
<p class="abs about-text">At Coral Basins, we specialize in designing and building bespoke swimming pools for those who demand perfection. Our philosophy blends innovative engineering, modern aesthetics, and enduring quality to deliver the ultimate luxury pool experience.</p>
<div class="btn" style="left:667px;top:1316px;width:173px;height:39px">Read More</div>

<!-- SERVICES -->
<h2 class="abs section-title" style="top:1503px">Crafting Exceptional Pool Experiences</h2>
<p class="abs section-sub" style="top:1567px">From design to maintenance, we bring precision, beauty, and<br>innovation to every pool we create.</p>

<div class="service-card" style="left:57px;width:336px;background:linear-gradient(160deg,#d9dcdc 0%,#9aa3a2 45%,#5d7460 75%,#8c6a4e 100%)" role="img" aria-label="Poolside loungers against a white wall with greenery">
  <h3 style="top:296px">Pool Design &amp;<br>Construction</h3>
  <p style="top:384px">We Specialize In Creating Bespoke Swimming Pools That Blend Architecture, Artistry, And Functionality.</p>
</div>
<div class="service-card" style="left:415px;width:352px;background:linear-gradient(200deg,#c9c6c2 0%,#8a7d72 35%,#3c6f8e 65%,#204d70 100%)" role="img" aria-label="Aerial view of a curved pool edged with wooden decking and loungers">
  <h3 style="top:292px">Renovation &amp;<br>Maintenance</h3>
  <p style="top:380px">Restore The Brilliance Of Your Pool With Our Professional Renovation And Maintenance Services.</p>
</div>
<div class="service-card" style="left:789px;width:354px;background:linear-gradient(160deg,#1d2b2a 0%,#2f4a3a 40%,#3e6b46 70%,#1a2422 100%)" role="img" aria-label="Dark stone spa shower room surrounded by tropical plants">
  <h3 style="top:278px">Spa &amp; Jacuzzi<br>Design</h3>
  <p style="top:366px">Indulge In The Art Of Relaxation With Our Spa And Jacuzzi Solutions.</p>
</div>
<div class="btn" style="left:504px;top:2227px;width:173px;height:39px">More Details</div>

<!-- STYLES -->
<h2 class="abs" style="left:57px;top:2374px;font-family:'Nunito Sans',sans-serif;font-weight:400;font-size:28px">Find Your Ideal Pool Style</h2>
<p class="abs" style="left:57px;top:2444px;font-size:22px;line-height:31px;color:var(--muted)">Discover 35 expertly designed ceramic pool shapes from sleek<br>modern lines to natural freeform beauty.</p>

<div class="photo" style="left:51px;top:2573px;width:337px;height:295px;background:linear-gradient(180deg,#4f7a44 0%,#7fae6a 35%,#5fd9cf 70%,#2bc3c0 100%)" role="img" aria-label="Geometric turquoise pool with steps and a green living wall"></div>
<div class="photo" style="left:419px;top:2573px;width:340px;height:295px;background:radial-gradient(circle at 50% 45%,#7ed3e6 0%,#3f9fb4 18%,#a2624e 32%,#3f6b35 60%,#2e5128 100%)" role="img" aria-label="Aerial view of a round freeform pool among tropical gardens"></div>
<div class="photo" style="left:789px;top:2573px;width:340px;height:295px;background:linear-gradient(180deg,#7fb6e0 0%,#4a98d4 40%,#2a7fc4 75%,#8fd0ef 100%)" role="img" aria-label="Family enjoying splashing in a bright blue pool"></div>

<div class="style-title" style="left:50px">Modern Geometric Pools</div>
<div class="style-title" style="left:419px">Freeform Natural Pools</div>
<div class="style-title" style="left:789px">Family-Friendly Pools</div>
<p class="style-desc" style="left:50px">Clean, minimalistic lines perfect for<br>contemporary homes.</p>
<p class="style-desc" style="left:419px">Inspired by nature, with curves and organic<br>shapes for a relaxing vibe.</p>
<p class="style-desc" style="left:789px">Safe and spacious designs ideal for kids<br>and gatherings.</p>
<div class="btn-outline" style="left:152px;top:3008px;width:135px;height:37px;border-color:#f0b27d">Details →</div>
<div class="btn-outline" style="left:522px;top:3008px;width:135px;height:37px;border-color:#f0b27d">Details →</div>
<div class="btn-outline" style="left:892px;top:3008px;width:135px;height:37px;border-color:#f0b27d">Details →</div>

<!-- TESTIMONIALS -->
<h2 class="abs" style="left:57px;top:3151px;font-family:'Nunito Sans',sans-serif;font-weight:400;font-size:28px">Real Stories from Our Customer</h2>
<div class="abs" style="left:57px;top:3230px;width:116px;height:8px;background:var(--blue)"></div>

<div class="review" style="left:51px">
  <div class="avatar" style="background:linear-gradient(180deg,#f3b23a,#e08a2a)" role="img" aria-label="Customer portrait"></div>
  <div class="stars"><svg width="150" height="22" viewBox="0 0 150 22"><g fill="var(--star)"><path id="s" d="M11 1l3 7 7.5.5-5.8 4.8 1.9 7.3L11 16.6 4.4 20.6l1.9-7.3L.5 8.5 8 8z"/><use href="#s" x="32"/><use href="#s" x="64"/><use href="#s" x="96"/><use href="#s" x="128"/></g></svg></div>
  <h4>Marla Quentin</h4>
  <p>"Coral Basins transformed our backyard into a private resort. Every detail — from the lighting to the waterline finish — reflects pure elegance and craftsmanship."</p>
</div>
<div class="review" style="left:535px">
  <div class="avatar" style="background:linear-gradient(180deg,#9fd6e8,#6fb4cc)" role="img" aria-label="Customer portrait"></div>
  <div class="stars"><svg width="150" height="22" viewBox="0 0 150 22"><g fill="var(--star)"><path id="s2" d="M11 1l3 7 7.5.5-5.8 4.8 1.9 7.3L11 16.6 4.4 20.6l1.9-7.3L.5 8.5 8 8z"/><use href="#s2" x="32"/><use href="#s2" x="64"/><use href="#s2" x="96"/><use href="#s2" x="128"/></g></svg></div>
  <h4>Theo Brannock</h4>
  <p>"Their design team understood exactly what we envisioned. The result is a timeless pool that enhances our home's architecture perfectly."</p>
</div>
<div class="review" style="left:1019px">
  <div class="avatar" style="background:linear-gradient(180deg,#f4c04a,#e39b2f)" role="img" aria-label="Customer portrait"></div>
  <h4 style="white-space:nowrap">Priya Lowell</h4>
  <p>"Maintenance has been effortless and the water quality remains crystal clear. Truly a five-star experience from start to finish."</p>
</div>

<div class="btn-outline" style="left:437px;top:3671px;width:126px;height:39px">Previous</div>
<div class="btn-outline" style="left:584px;top:3671px;width:134px;height:39px">Next</div>

<!-- CONTACT -->
<section class="abs contact">
  <h2>Contact</h2>
  <p class="lead">Get in touch with our team to explore how Coral Basins<br>can power your next-generation pool project.</p>

  <div class="ico" style="top:348px"><svg width="26" height="26" viewBox="0 0 24 24"><path fill="#fff" d="M6.6 10.8a15.1 15.1 0 006.6 6.6l2.2-2.2c.3-.3.7-.4 1-.2 1.1.4 2.3.6 3.6.6.6 0 1 .4 1 1V20c0 .6-.4 1-1 1A17 17 0 013 4c0-.6.4-1 1-1h3.5c.6 0 1 .4 1 1 0 1.3.2 2.5.6 3.6.1.3 0 .7-.2 1z"/></svg></div>
  <div class="info" style="top:364px"><b>CALL US</b>+1 (410) 555-0192</div>

  <div class="ico solid" style="top:442px"><svg width="28" height="22" viewBox="0 0 28 22"><rect x="1" y="1" width="26" height="20" rx="3" fill="var(--navy)"/><path d="M2 3l12 9 12-9" stroke="#fff" stroke-width="2" fill="none"/></svg></div>
  <div class="info" style="top:458px"><b>EMAIL</b>hello@coralbasins.co</div>

  <div class="ico solid" style="top:535px"><svg width="22" height="30" viewBox="0 0 22 30"><path d="M11 0C4.9 0 0 4.9 0 11c0 8 11 19 11 19s11-11 11-19C22 4.9 17.1 0 11 0z" fill="var(--navy)"/><circle cx="11" cy="11" r="4" fill="#fff"/></svg></div>
  <div class="info" style="top:552px"><b>LOCATION</b>48 Harbor Crest Lane,<br>Annapolis, Maryland, USA</div>

  <div class="field-label" style="top:118px">NAME</div>
  <div class="field" style="top:153px;height:63px"></div>
  <div class="field-label" style="top:238px">EMAIL ADDRESS</div>
  <div class="field" style="top:273px;height:63px"></div>
  <div class="field-label" style="top:366px">PHONE</div>
  <div class="field" style="top:401px;height:61px"></div>
  <div class="field-label" style="top:504px">MESSAGE</div>
  <div class="field" style="top:542px;height:148px"></div>
  <div class="submit">SUBMIT</div>
</section>

<!-- FOOTER -->
<footer class="footer">
  <div class="abs" style="left:134px;top:4871px;width:82px;height:82px;border-radius:50%;background:var(--navy)"></div>
  <div class="abs" style="left:120px;top:4962px;width:110px;text-align:center;font-weight:600;font-size:12px;color:var(--navy)">CORAL BASINS</div>
  <svg class="abs" style="left:86px;top:4984px" width="24" height="24" viewBox="0 0 24 24"><path fill="none" stroke="var(--navy)" stroke-width="1.6" d="M6.6 10.8a15.1 15.1 0 006.6 6.6l2.2-2.2c.3-.3.7-.4 1-.2 1.1.4 2.3.6 3.6.6.6 0 1 .4 1 1V20c0 .6-.4 1-1 1A17 17 0 013 4c0-.6.4-1 1-1h3.5c.6 0 1 .4 1 1 0 1.3.2 2.5.6 3.6.1.3 0 .7-.2 1z"/></svg>
  <div class="foot-link" style="left:132px;top:4984px;font-size:13px">Give Us a Call :</div>
  <div class="foot-link" style="left:132px;top:5004px;font-weight:600;color:#123">+14105550176</div>
  <svg class="abs" style="left:88px;top:5054px" width="22" height="18" viewBox="0 0 22 18"><rect x="1" y="1" width="20" height="16" rx="2" fill="none" stroke="var(--navy)" stroke-width="1.6"/><path d="M2 3l9 7 9-7" fill="none" stroke="var(--navy)" stroke-width="1.6"/></svg>
  <div class="foot-link" style="left:132px;top:5052px;font-size:13px">Email :</div>
  <div class="foot-link" style="left:132px;top:5074px;font-weight:600;color:#123">hello@coralbasins.co</div>

  <div class="foot-head" style="left:360px">QUICK LINKS</div>
  <div class="foot-link" style="left:360px;top:4957px">Home</div>
  <div class="foot-link" style="left:360px;top:4989px">About Us</div>
  <div class="foot-link" style="left:360px;top:5017px">Services<br>Section</div>
  <div class="foot-link" style="left:360px;top:5073px">Pool Styles</div>
  <div class="foot-link" style="left:486px;top:4955px">Testimony</div>
  <div class="foot-link" style="left:486px;top:4987px">Contact</div>

  <div class="foot-head" style="left:592px">SITE INFORMATION</div>
  <div class="foot-link" style="left:592px;top:4961px">Privacy Policy</div>
  <div class="foot-link" style="left:592px;top:4995px">Terms of Use</div>
  <div class="foot-link" style="left:592px;top:5024px">Accessibility Statement</div>

  <div class="abs" style="left:824px;top:4913px;width:300px;font-weight:600;font-size:13px;line-height:22px;color:var(--navy)">SIGN UP FOR FREE RESOURCES FROM<br>OUR TEAM.</div>
  <div class="abs" style="left:824px;top:4975px;width:307px;height:41px;background:var(--navy)"></div>
  <div class="abs" style="left:842px;top:4989px;font-size:10px;color:rgba(255,255,255,.8)">Your Email Address</div>
  <div class="abs" style="left:1024px;top:4982px;width:99px;height:27px;border:1px solid #fff;display:flex;align-items:center;justify-content:center;font-weight:600;font-size:10px;color:#fff">Subscribe</div>
  <div class="abs" style="left:829px;top:5062px;font-weight:600;font-size:13px;color:var(--navy)">FOLLOW US</div>
  <div class="abs" style="left:830px;top:5096px;width:12px;height:12px;border-radius:50%;background:var(--navy)"></div>
  <div class="abs" style="left:856px;top:5096px;width:12px;height:12px;border-radius:50%;background:var(--navy)"></div>
  <div class="abs" style="left:882px;top:5096px;width:12px;height:12px;border-radius:50%;background:var(--navy)"></div>

  <div class="abs copy">© 2025 Coral Basins. All Rights Reserved.</div>
</footer>

</body>
</html>
```